HIGH-END ANTI AGING START-UP NEEDS DOCUMENT/LETTERHEAD DESIGN!!!!

We are a high end anti-aging and health start-up catering to clients in Stamford and NYC. We just did a logo redesign and are now looking for a letter head design that we can use IN GOOGLE DOCS for marwickcaregroup.example clients. We are REALLY EXCITED to see what you can show us!!!!!!!! We need something sophisticated and MODERN! Thanks so much!

Target Market(s)

High end, boutique medical clients. Our clientele is fairly high profile and we need a sleek, sophisticated letter head to put on all of our marketing materials and medical forms as well.

Industry/Entity Type

Medical

Font styles to use
Serif
Sans Serif

Colors
0255a3
ffffff
00a990
1b1b1b
919191

Requirements
Must have
• Must have the logo and "Marwick Care Group" written somewhere. Must have our URL www.marwickcaregroup.example.
Nice to have
• office phone number (203) 555-0147
Should not have
• Colors outside of our logo colors + grey + black

```html
<!DOCTYPE html>
<html lang="en">
<head>
<meta charset="utf-8">
<title>Marwick Care Group Letterhead</title>
<link href="https://fonts.googleapis.com/css2?family=Open+Sans:wght@400;600;700&display=swap" rel="stylesheet">
<style>
  :root {
    --backdrop: #8a8279;
    --paper: #ffffff;
    --brand-blue: #4a72b8;
    --brand-green: #00964a;
    --ink: #1b1b1b;
  }
  html, body {
    margin: 0;
    width: 1200px;
    height: 795px;
    overflow: hidden;
    background: var(--backdrop);
    font-family: "Open Sans", Arial, sans-serif;
  }
  .letterhead {
    position: absolute;
    left: 320px;
    top: 26px;
    width: 560px;
    height: 742px;
    background: var(--paper);
    box-shadow: 0 8px 24px rgba(0,0,0,0.25);
    overflow: hidden;
  }
  .brand-mark {
    position: absolute;
    left: 60px;
    top: 62px;
    display: flex;
    align-items: center;
    gap: 10px;
  }
  .brand-mark__dot {
    width: 26px;
    height: 26px;
    border-radius: 50%;
    background: var(--brand-green);
  }
  .brand-mark__name {
    font-weight: 700;
    font-size: 17px;
    color: var(--brand-blue);
    letter-spacing: 0.02em;
  }
  .corner-accent {
    position: absolute;
    right: -70px;
    top: 300px;
    width: 190px;
    height: 190px;
    border-radius: 50%;
    background: var(--brand-green);
  }
  .contact-block {
    position: absolute;
    left: 60px;
    bottom: 52px;
    font-size: 11px;
    line-height: 1.55;
    color: var(--ink);
  }
  .contact-block__name {
    font-weight: 700;
    font-size: 12px;
    margin: 0 0 1px;
  }
  .contact-block__name .first { color: var(--brand-blue); }
  .contact-block__name .rest { color: var(--brand-green); }
  .contact-block__line {
    display: flex;
    align-items: center;
    gap: 6px;
    margin: 0;
  }
  .contact-icon {
    width: 12px;
    height: 12px;
    flex: none;
  }
</style>
</head>
<body>
  <main class="letterhead">
    <div class="brand-mark">
      <span class="brand-mark__dot"></span>
      <span class="brand-mark__name">Marwick Care Group</span>
    </div>

    <div class="corner-accent"></div>

    <address class="contact-block" style="font-style:normal">
      <p class="contact-block__name"><span class="first">Marwick</span> <span class="rest">Care Group</span></p>
      <p class="contact-block__line">18 Elm St. Suite 410, Stamford CT, 06901</p>
      <p class="contact-block__line">
        <svg class="contact-icon" viewBox="0 0 12 12" aria-hidden="true"><circle cx="6" cy="6" r="6" fill="var(--brand-green)"/><path d="M4 3.2l1 1.2-.6.8c.4.9 1 1.5 1.9 1.9l.8-.6 1.2 1-.7 1C5.8 8.3 3.7 6.2 3.5 3.9z" fill="#fff"/></svg>
        (203) 555-0147
      </p>
      <p class="contact-block__line">
        <svg class="contact-icon" viewBox="0 0 12 12" aria-hidden="true"><circle cx="6" cy="6" r="6" fill="var(--brand-green)"/><rect x="3" y="4" width="6" height="4.2" fill="none" stroke="#fff" stroke-width=".9"/><path d="M3 4l3 2.3L9 4" fill="none" stroke="#fff" stroke-width=".9"/></svg>
        info@marwickcaregroup.example
      </p>
      <p class="contact-block__line">
        <svg class="contact-icon" viewBox="0 0 12 12" aria-hidden="true"><circle cx="6" cy="6" r="6" fill="var(--brand-green)"/><circle cx="6" cy="6" r="3.2" fill="none" stroke="#fff" stroke-width=".8"/><path d="M2.8 6h6.4M6 2.8c-1.4 1.8-1.4 4.6 0 6.4M6 2.8c1.4 1.8 1.4 4.6 0 6.4" fill="none" stroke="#fff" stroke-width=".7"/></svg>
        www.marwickcaregroup.example
      </p>
    </address>
  </main>
</body>
</html>
```